Website Redesign for Accommodation Directory

We need a redesign for stayfinderhubzone.example
The new design needs to include a banner with overlaid text and a 'get started now' button. The overlaid text could be 'Find Hotels in Auckland, New Zealand' for example.
The new design needs to include:
- primary navigation in header
- an accommodation search (left or right column)
- a secondary navigation menu (under the search).
We will need the following font styles (including links for each) defined also please:
h1, h2, h3, h4, h5, h6, p, ul, ol, address, pre
Accommodation

```html
<!DOCTYPE html>
<html lang="en">
<head>
<meta charset="utf-8">
<title>stayfinderhubzone – Find Hotels</title>
<link href="https://fonts.googleapis.com/css2?family=Source+Sans+3:ital,wght@0,400;0,600;0,700;1,400&display=swap" rel="stylesheet">
<style>
:root{
  --red:#e2231a;
  --red-dark:#b5120c;
  --text:#333;
  --grey-bg:#efefef;
  --white:#fff;
  --black:#050505;
}
*{margin:0;padding:0;box-sizing:border-box}
html,body{width:836px;height:1200px;overflow:hidden}
body{position:relative;background:var(--white);font-family:"Source Sans 3",Arial,sans-serif;color:var(--text)}
.abs{position:absolute}
a{color:inherit;text-decoration:none}

/* top bar */
.top-bar{left:0;top:0;width:836px;height:43px;background:var(--black)}
.top-links{left:0;top:0;width:836px;height:43px;font-size:11.5px;color:var(--white)}
.top-links a,.top-links span{position:absolute;top:14px}
.social{display:flex;gap:8px}
.social i{display:block;width:22px;height:22px;border-radius:50%}
.social .s1{background:#3b5998}.social .s2{background:#2bb3e6}.social .s3{background:#f28a1b}.social .s4{background:#eeeeee}
.top-social{left:692px;top:11px}

/* header */
.header-bg{left:0;top:43px;width:836px;height:262px;background:var(--grey-bg)}
.brand-name{left:0;top:58px;width:836px;text-align:center;font-size:40px;font-weight:600;color:#5a5a5a;line-height:46px}

/* banner */
.banner-frame{left:24px;top:125px;width:788px;height:295px;background:linear-gradient(#e4e4e4,#cfcfcf);border-radius:24px 24px 60px 60px/24px 24px 40px 40px}
.banner-shadow{left:40px;top:420px;width:756px;height:18px;background:radial-gradient(ellipse at top,rgba(0,0,0,.18),transparent 70%)}
.banner-photo{left:40px;top:140px;width:756px;height:258px;border-radius:20px 20px 40px 40px/20px 20px 26px 26px;background:linear-gradient(160deg,#3a3324 0%,#1c8fb0 35%,#5fd2e8 55%,#c9b18a 75%,#5a4a30 100%)}
.banner-title{left:67px;top:171px;font-size:30px;font-weight:400;color:var(--white);text-shadow:0 1px 3px rgba(0,0,0,.5);line-height:38px}
.cta{left:474px;top:351px;width:238px;height:40px;border-radius:20px;background:linear-gradient(#f2443a,var(--red-dark));color:var(--white);font-size:24px;line-height:38px;padding-left:17px;box-shadow:0 2px 4px rgba(0,0,0,.4)}
.cta-knob{right:0;top:0;width:40px;height:40px}

/* navigation */
.main-nav{left:24px;top:448px;width:784px;height:34px}
.nav-links{left:0;top:0;width:100%;height:34px;font-size:15px;color:var(--white)}
.nav-links a{position:absolute;top:7px}
.nav-active{left:446px;top:0;width:133px;height:36px;background:var(--white)}
.nav-links a.active{color:var(--red)}
.dropdown{left:471px;top:484px;width:130px;background:var(--white);padding:1px;box-shadow:0 2px 4px rgba(0,0,0,.3)}
.dropdown a{display:flex;align-items:center;gap:9px;height:17px;margin-bottom:2px;background:var(--red);color:var(--white);font-size:9.5px;padding-left:8px}
.dbl{width:10px;height:8px}

/* main */
.section-title{font-size:20px;font-weight:400;color:#555;text-decoration:underline;text-decoration-thickness:1px;text-underline-offset:3px;line-height:26px}
.thumb{width:165px;height:85px;border-radius:6px}
.t1{background:linear-gradient(#6c7f88,#3e2c22)}
.t2{background:linear-gradient(#7a1515,#3a0b0b)}
.t3{background:linear-gradient(#c28a3a,#5b3a1c)}
.caption{width:160px;font-size:10px;line-height:12px;color:#222}
.lead{left:26px;top:697px;width:490px;font-size:12.5px;font-style:italic;color:var(--red);line-height:16.5px}
.body-copy{left:24px;top:757px;width:266px;font-size:10.5px;line-height:13.2px;color:#222}
.body-copy p+p{margin-top:12px}
.welcome-photo{left:300px;top:760px;width:200px;height:122px;border-radius:10px;background:linear-gradient(135deg,#4a2c14,#c98a46 55%,#6b4323)}
.read-more{left:222px;top:885px;font-size:9.5px;color:var(--red)}

/* side */
.side-box{background:var(--white);border:1px solid #d6d6d6;border-radius:16px;box-shadow:0 2px 4px rgba(0,0,0,.12)}
.side-title{font-size:19px;font-weight:400;color:var(--red);line-height:24px}
.select{left:570px;width:218px;height:22px;border:1px solid #ccc;background:linear-gradient(#fff,#f1f1f1);font-size:9.5px;padding:4px 0 0 6px;color:#222}
.select svg{position:absolute;right:8px;top:7px}
.search-btn{left:723px;top:593px;width:65px;height:21px;border-radius:11px;border:1px solid #ccc;background:linear-gradient(#fff,#e3e3e3);font-size:11px;color:var(--red);text-align:center;line-height:19px}
.tert-list{left:570px;top:675px;width:215px;list-style:none}
.tert-list li{height:33.5px;border-bottom:1px solid #eee;display:flex;align-items:center;font-size:9.5px;color:#444}
.tert-list li:last-child{border-bottom:none}
.tert-list svg{margin:0 33px 0 9px}

/* footer */
.footer-band{left:0;top:906px;width:836px;height:190px;background:linear-gradient(#dcdcdc,#f7f7f7 30%,#f2f2f2 85%,#dedede)}
.divider{top:918px;width:1px;height:150px;background:#cfcfcf}
.footer-title{font-size:20px;font-weight:400;color:var(--red-dark);line-height:26px}
.avatar{width:36px;height:40px;border-radius:18px 18px 4px 4px;background:linear-gradient(#3b3b3b,#111)}
.news-text{width:165px;font-size:9.5px;font-weight:600;line-height:12.5px;color:#333}
.field{width:148px;height:24px;border-radius:5px;background:linear-gradient(#e2e2e2,#fff);border:1px solid #ddd;box-shadow:inset 0 1px 2px rgba(0,0,0,.15)}
.btn-dark{height:21px;border-radius:6px;background:linear-gradient(#555,#000);color:var(--white);font-size:12px;text-align:center;line-height:20px}

.bottom-bar{left:0;top:1108px;width:836px;height:44px;background:var(--black)}
.bottom-links{font-size:11.5px;color:var(--white)}
.bottom-links a{position:absolute;top:14px}
.bottom-social{left:683px;top:11px}
.copyright{left:0;top:1163px;width:836px;text-align:center;font-size:10px;color:#333}
</style>
</head>
<body>

<header>
  <div class="abs top-bar">
    <nav class="abs top-links">
      <a href="#" style="left:32px">Free Insurance Quotes</a><span style="left:151px">|</span>
      <a href="#" style="left:170px">Free Website Statistics</a><span style="left:298px">|</span>
      <a href="#" style="left:321px">Company Reviews</a>
    </nav>
    <div class="abs social top-social"><i class="s1"></i><i class="s2"></i><i class="s3"></i><i class="s4"></i></div>
  </div>
  <div class="abs header-bg"></div>
  <div class="abs brand-name">stayfinderhubzone</div>

  <div class="abs banner-frame"></div>
  <div class="abs banner-shadow"></div>
  <div class="abs banner-photo" role="img" aria-label="Night view of a resort with a lit swimming pool, pool bar and terrace seating"></div>
  <h1 class="abs banner-title">Find Hotels in Auckland, New Zealand</h1>
  <a href="#" class="abs cta">Get Started Now
    <svg class="abs cta-knob" viewBox="0 0 40 40"><circle cx="20" cy="20" r="18" fill="#f3f3f3" stroke="#ccc"/><path d="M25 12 L13 20 L25 28 Z" fill="#c9c9c9"/></svg>
  </a>

  <nav class="abs main-nav">
    <svg class="abs" style="left:0;top:0" width="784" height="34" viewBox="0 0 784 34">
      <defs><linearGradient id="ribbon" x1="0" y1="0" x2="0" y2="1"><stop offset="0" stop-color="#f04a3f"/><stop offset="1" stop-color="#c8150e"/></linearGradient></defs>
      <path d="M0 0 H784 L762 17 L784 34 H0 L22 17 Z" fill="url(#ribbon)"/>
    </svg>
    <div class="abs nav-active"></div>
    <div class="abs nav-links">
      <a href="#" style="left:86px">Home</a>
      <a href="#" style="left:169px">Add Your Property</a>
      <a href="#" style="left:329px">Supplier Login</a>
      <a href="#" class="active" style="left:459px">Accommodation</a>
      <a href="#" style="left:583px">Contact Us</a>
    </div>
  </nav>
</header>

<main>
  <h2 class="abs section-title" style="left:28px;top:494px">Featured Accommodations</h2>
  <div class="abs thumb t1" style="left:28px;top:525px" role="img" aria-label="Villa with a pool"></div>
  <div class="abs thumb t2" style="left:201px;top:525px" role="img" aria-label="Hotel lounge with red furnishings"></div>
  <div class="abs thumb t3" style="left:375px;top:525px" role="img" aria-label="Hotel bedroom"></div>
  <p class="abs caption" style="left:33px;top:617px">Lorem Ipsum is simply dummy text of the printing and typesetting industry.</p>
  <p class="abs caption" style="left:206px;top:617px">Lorem Ipsum is simply dummy text of the printing and typesetting industry.</p>
  <p class="abs caption" style="left:380px;top:617px">Lorem Ipsum is simply dummy text of the printing and typesetting industry.</p>

  <h2 class="abs section-title" style="left:26px;top:666px;font-size:19px">Welcome to &nbsp;Our Website</h2>
  <p class="abs lead">You've come to the right place to find Accommodation in Any Country whether it's a hotel, motel, backpackers, bed and breakfast or beach house you're after you'll find just what you need to enjoy your stay in Any Country.</p>
  <div class="abs body-copy">
    <p>With much to choose from you'll want to find a place that meets your needs. Our accommodation search tool will help you find the perfect place, regardless of what your price, location or style requirements might be.</p>
    <p>Our Any Country accommodation directory is perfect for times when you've scored cheap flights, desperately need last-minute accommodation or are just planning your next holiday or business trip to Any Country.</p>
  </div>
  <div class="abs welcome-photo" role="img" aria-label="Warmly lit hotel suite with bed and dining table"></div>
  <a href="#" class="abs read-more">Read more...</a>

  <aside>
    <div class="abs side-box" style="left:553px;top:498px;width:247px;height:130px"></div>
    <h3 class="abs side-title" style="left:569px;top:507px">Accommodation Search</h3>
    <div class="abs select" style="top:539px">All Countries<svg width="10" height="8" viewBox="0 0 10 8"><path d="M0 0H10L5 8Z" fill="#e2231a"/></svg></div>
    <div class="abs select" style="top:565px">All Categories<svg width="10" height="8" viewBox="0 0 10 8"><path d="M0 0H10L5 8Z" fill="#e2231a"/></svg></div>
    <div class="abs search-btn">Search</div>

    <div class="abs side-box" style="left:553px;top:636px;width:247px;height:246px"></div>
    <h3 class="abs side-title" style="left:578px;top:644px">Tertiary navigation</h3>
    <ul class="abs tert-list">
      <li><svg width="10" height="8" viewBox="0 0 10 8"><path d="M0 0L5 4L0 8ZM5 0L10 4L5 8Z" fill="#e2231a"/></svg><a href="#">Type your link here</a></li>
      <li><svg width="10" height="8" viewBox="0 0 10 8"><path d="M0 0L5 4L0 8ZM5 0L10 4L5 8Z" fill="#e2231a"/></svg><a href="#">Type your link here</a></li>
      <li><svg width="10" height="8" viewBox="0 0 10 8"><path d="M0 0L5 4L0 8ZM5 0L10 4L5 8Z" fill="#e2231a"/></svg><a href="#">Type your link here</a></li>
      <li><svg width="10" height="8" viewBox="0 0 10 8"><path d="M0 0L5 4L0 8ZM5 0L10 4L5 8Z" fill="#e2231a"/></svg><a href="#">Type your link here</a></li>
      <li><svg width="10" height="8" viewBox="0 0 10 8"><path d="M0 0L5 4L0 8ZM5 0L10 4L5 8Z" fill="#e2231a"/></svg><a href="#">Type your link here</a></li>
      <li><svg width="10" height="8" viewBox="0 0 10 8"><path d="M0 0L5 4L0 8ZM5 0L10 4L5 8Z" fill="#e2231a"/></svg><a href="#">Type your link here</a></li>
    </ul>
  </aside>

  <div class="abs dropdown">
    <a href="#"><svg class="dbl" viewBox="0 0 10 8"><path d="M0 0L5 4L0 8ZM5 0L10 4L5 8Z" fill="#fff"/></svg>Type your link here</a>
    <a href="#"><svg class="dbl" viewBox="0 0 10 8"><path d="M0 0L5 4L0 8ZM5 0L10 4L5 8Z" fill="#fff"/></svg>Type your link here</a>
    <a href="#" style="margin-bottom:0"><svg class="dbl" viewBox="0 0 10 8"><path d="M0 0L5 4L0 8ZM5 0L10 4L5 8Z" fill="#fff"/></svg>Type your link here</a>
  </div>
</main>

<footer>
  <div class="abs footer-band"></div>
  <div class="abs divider" style="left:276px"></div>
  <div class="abs divider" style="left:494px"></div>

  <h3 class="abs footer-title" style="left:87px;top:917px">Latest News</h3>
  <div class="abs avatar" style="left:42px;top:960px" role="img" aria-label="Author portrait"></div>
  <p class="abs news-text" style="left:88px;top:963px">Lorem Ipsum is simply dummy text of the printing and typesetting industry.</p>
  <div class="abs avatar" style="left:42px;top:1018px" role="img" aria-label="Author portrait"></div>
  <p class="abs news-text" style="left:90px;top:1019px">Lorem Ipsum is simply dummy text of the printing and typesetting industry.</p>

  <h3 class="abs footer-title" style="left:326px;top:914px">News Letter</h3>
  <div class="abs field" style="left:309px;top:954px"></div>
  <div class="abs field" style="left:309px;top:988px"></div>
  <div class="abs btn-dark" style="left:330px;top:1036px;width:90px">Subscribe</div>

  <h3 class="abs footer-title" style="left:571px;top:914px">Contact</h3>
  <div class="abs field" style="left:543px;top:950px"></div>
  <div class="abs field" style="left:543px;top:984px"></div>
  <div class="abs field" style="left:543px;top:1018px;height:57px"></div>
  <div class="abs btn-dark" style="left:698px;top:1054px;width:90px">Submit</div>

  <div class="abs bottom-bar">
    <nav class="abs bottom-links" style="left:0;top:0;width:836px;height:44px">
      <a href="#" style="left:36px">Home</a>
      <a href="#" style="left:100px">Add Your Property</a>
      <a href="#" style="left:225px">Supplier Login</a>
      <a href="#" style="left:326px">Accommodation</a>
      <a href="#" style="left:445px">Contact Us</a>
    </nav>
    <div class="abs social bottom-social"><i class="s1"></i><i class="s2"></i><i class="s3"></i><i class="s4"></i></div>
  </div>
  <p class="abs copyright">Copyright © 2011. www.stayfinderhubzone.example</p>
</footer>

</body>
</html>
```